VELKORIS Stationery Design Project

I want a stationery design for a web development company consists of:
1- business card
2- Letter Head
3- small Envelope
4- Large Envelope

need a very clean professional simple design yet creative,

The company logo is attached
http://www.pixelbazaarhub.net/project-progress/designs.aspx?briefId=5830174&submissionId=47210938

logo font is sui generis rg (attached)
I would like to have the stationery text font to be helvetica font regular or light (can be changed)

I love the combination of cyan, black and grey colors
( will attach some recommended styles)

Business

• curves or waves

```html
<!DOCTYPE html>
<html lang="en">
<head>
<meta charset="utf-8">
<title>VELKORIS Business Card</title>
<link rel="stylesheet" href="https://fonts.googleapis.com/css2?family=Arimo:wght@400;700&display=swap">
<style>
  :root {
    --cyan: #129fdb;
    --ink: #2b2d30;
    --grey: #8d9094;
    --text-grey: #5f6367;
    --paper: #f7f9fa;
    --backdrop: #dcdbe9;
  }
  * { box-sizing: border-box; margin: 0; padding: 0; }
  html, body {
    width: 1200px; height: 906px; overflow: hidden;
    background: var(--backdrop);
    font-family: "Arimo", Helvetica, Arial, sans-serif;
  }
  .sheet {
    width: 1200px; height: 906px;
    display: flex; align-items: center; justify-content: center; gap: 40px;
  }
  .card {
    position: relative;
    width: 540px; height: 309px;
    background: var(--paper);
    overflow: hidden;
    box-shadow: 0 6px 18px rgba(60, 60, 90, 0.18);
  }
  .card-shapes { position: absolute; inset: 0; width: 100%; height: 100%; }
  .wordmark {
    position: absolute;
    display: flex; align-items: center; gap: 10px;
    color: var(--cyan);
    font-weight: 700;
    letter-spacing: 2px;
  }
  .wordmark-square { width: 14px; height: 14px; background: var(--cyan); }

  /* back side */
  .card-back .wordmark {
    left: 0; right: 0; top: 92px;
    justify-content: center;
    font-size: 40px;
  }
  .card-back .web-address {
    position: absolute; left: 0; right: 0; bottom: 48px;
    text-align: center;
    color: #ffffff; font-size: 13px; letter-spacing: 0.5px;
  }
  .web-address .domain { color: var(--cyan); }

  /* front side */
  .card-front .wordmark {
    left: 40px; top: 150px;
    font-size: 30px;
  }
  .contact { position: absolute; left: 290px; top: 46px; width: 230px; }
  .contact-name {
    color: var(--cyan); font-size: 17px; letter-spacing: 0.5px;
  }
  .contact-title { color: var(--text-grey); font-size: 11.5px; margin-top: 3px; padding-left: 8px; }
  .contact-address {
    margin-top: 16px; padding-left: 18px;
    border-left: 3px solid var(--cyan);
    color: var(--text-grey); font-size: 11.5px; line-height: 1.45;
  }
  .contact-lines {
    list-style: none;
    margin-top: 14px; margin-left: 30px; padding-left: 18px;
    border-left: 1px solid var(--grey);
    color: var(--text-grey); font-size: 11.5px; line-height: 1.55;
  }
  .contact-lines li { display: flex; align-items: center; gap: 8px; }
  .contact-icon { width: 11px; height: 11px; flex: none; }
</style>
</head>
<body>
<main class="sheet">

  <section class="card card-back" aria-label="Business card back">
    <svg class="card-shapes" viewBox="0 0 540 309" aria-hidden="true">
      <polygon points="290,174 540,125 540,160" fill="var(--cyan)"/>
      <polygon points="0,190 540,160 540,309 0,309" fill="var(--ink)"/>
    </svg>
    <div class="wordmark"><span class="wordmark-square"></span>VELKORIS</div>
    <p class="web-address">www.<span class="domain">velkoris</span>.com</p>
  </section>

  <section class="card card-front" aria-label="Business card front">
    <svg class="card-shapes" viewBox="0 0 540 309" aria-hidden="true">
      <polygon points="0,288 250,300 250,309 0,309" fill="var(--grey)"/>
      <polygon points="250,300 540,160 540,205 340,309 250,309" fill="var(--cyan)"/>
    </svg>
    <div class="wordmark"><span class="wordmark-square"></span>VELKORIS</div>

    <div class="contact">
      <h1 class="contact-name">MAREK TOLVAN</h1>
      <p class="contact-title">General Manager</p>
      <p class="contact-address">4816 Calloway Drive, Suite 140<br>Brenford, TX 77510</p>
      <ul class="contact-lines">
        <li>
          <svg class="contact-icon" viewBox="0 0 12 12" aria-hidden="true"><path d="M2.5 1 L4.5 1 L5.2 3.6 L4 4.6 Q5 7 7.4 8 L8.4 6.8 L11 7.5 L11 9.5 Q10.5 11 9 11 Q1 10 1 2.5 Q1 1 2.5 1Z" fill="var(--cyan)"/></svg>
          555-310-4826
        </li>
        <li>
          <svg class="contact-icon" viewBox="0 0 12 12" aria-hidden="true"><rect x="0.5" y="2.5" width="11" height="7" fill="var(--cyan)"/><path d="M0.5 2.5 L6 6.5 L11.5 2.5" stroke="#fff" stroke-width="1" fill="none"/></svg>
          info@velkoris.com
        </li>
        <li>
          <svg class="contact-icon" viewBox="0 0 12 12" aria-hidden="true"><g fill="none" stroke="var(--cyan)" stroke-width="1"><circle cx="6" cy="6" r="5"/><ellipse cx="6" cy="6" rx="2.2" ry="5"/><line x1="1" y1="6" x2="11" y2="6"/></g></svg>
          www.velkoris.com
        </li>
      </ul>
    </div>
  </section>

</main>
</body>
</html>
```